Kestrel Valley Alpine Riders Society needs a business card design

We need a business card design for our newly incorporated KVARS. We are helping the NZ Chinese community, as well as everyone else, to organise ski & snowboarding trips, training, and equipments. The design should be creative, energetic, young and vibrant.

Industry/Entity Type

Social Club

Contact Information for Business Card

Logo; Kestrel Valley Alpine Riders Society; Name: Oliver Brandt; Position: President; Address: 42 Marwick Rd, Epsom, Auckland 1051; Mobile: 020 7826 1957; Email: oliver@kvars-club.example; Web: www.kvars-club.example

Requirements
Must have
• 1, The text "Kestrel Valley Alpine Riders Society" should be put together with the supplied logo file to form a new complete logo combination.
• 2, Final design files should be in Adobe Illustrator format and all text must be editable.
Nice to have
• two or three colours

```html
<!DOCTYPE html>
<html lang="en">
<head>
<meta charset="utf-8">
<title>Kestrel Valley Alpine Riders Society – Business Card</title>
<link rel="stylesheet" href="https://fonts.googleapis.com/css2?family=Montserrat:wght@400;700;800&display=swap">
<style>
  :root {
    --sky-top: #d6eef3;
    --sky-bottom: #a8d9e7;
    --strip: #97d1e3;
    --snow: #ffffff;
    --navy: #1e3e8c;
    --bright-blue: #2a9fd8;
    --grey-text: #555b61;
    --page: #eceff1;
    --gear-a: #3d8fd6;
    --gear-b: #1e5fb4;
  }
  * { box-sizing: border-box; margin: 0; padding: 0; }
  html, body {
    width: 1200px; height: 1200px; overflow: hidden;
    background: var(--page);
    font-family: "Montserrat", sans-serif;
  }
  .card {
    position: absolute; left: 181px; width: 838px;
    overflow: hidden;
    box-shadow: 0 6px 14px rgba(0,0,0,.22);
  }
  .card-front { top: 196px; height: 389px; }
  .card-back { top: 624px; height: 384px; }
  .card-art { position: absolute; inset: 0; width: 100%; height: 100%; display: block; }

  .brand-name {
    position: absolute;
    font-weight: 800; color: var(--navy);
    letter-spacing: 1px; line-height: 1;
  }
  .card-front .brand-name { left: 44px; top: 58px; font-size: 68px; }
  .card-back .brand-name { left: 322px; top: 96px; width: 320px; text-align: center; font-size: 84px; }

  .person {
    position: absolute; right: 42px; top: 44px; text-align: right;
    color: var(--grey-text);
  }
  .person-name { font-size: 42px; line-height: 1.05; font-weight: 400; color: var(--bright-blue); }
  .person-name b { font-weight: 700; color: var(--navy); }
  .person-role { font-size: 17px; margin-top: 2px; }
  .person-mobile { font-size: 19px; margin-top: 2px; }

  .contact {
    position: absolute; left: 0; right: 0; top: 240px; text-align: center;
    font-size: 21px; line-height: 40px; color: var(--bright-blue);
  }
  .contact .label { font-weight: 700; color: var(--navy); }
  .contact .address-line { font-size: 25px; }

  .web-mark {
    position: absolute; left: 430px; top: 212px;
    font-size: 16px; font-weight: 700; color: var(--navy); letter-spacing: .5px;
  }
</style>
</head>
<body>

<section class="card card-front">
  <svg class="card-art" viewBox="0 0 838 389" aria-hidden="true">
    <defs>
      <linearGradient id="skyFront" x1="0" y1="0" x2="0" y2="1">
        <stop offset="0" stop-color="var(--sky-top)"/>
        <stop offset="1" stop-color="var(--sky-bottom)"/>
      </linearGradient>
    </defs>
    <rect width="838" height="206" fill="url(#skyFront)"/>
    <rect y="206" width="838" height="138" fill="var(--snow)"/>
    <polygon points="680,206 712,174 744,206" fill="var(--snow)"/>
    <rect y="344" width="838" height="45" fill="var(--strip)"/>
    <g fill="var(--snow)">
      <circle cx="30" cy="24" r="4"/><circle cx="226" cy="22" r="4"/>
      <circle cx="300" cy="74" r="4"/><circle cx="375" cy="95" r="4"/>
      <circle cx="410" cy="34" r="4"/><circle cx="450" cy="175" r="4"/>
      <circle cx="392" cy="158" r="4"/><circle cx="539" cy="48" r="4"/>
      <circle cx="600" cy="116" r="4"/><circle cx="625" cy="24" r="4"/>
      <circle cx="680" cy="58" r="4"/><circle cx="272" cy="188" r="4"/>
      <circle cx="818" cy="30" r="4"/><circle cx="590" cy="198" r="4"/>
      <circle cx="688" cy="360" r="4"/><circle cx="130" cy="180" r="4"/>
    </g>
  </svg>
  <div class="brand-name">KVARS</div>
  <div class="person">
    <div class="person-name">Oliver<b>Brandt</b></div>
    <div class="person-role">(PRESIDENT)</div>
    <div class="person-mobile">Mobile : 020 7826 1957</div>
  </div>
  <div class="contact">
    <p><span class="label">Email:</span> oliver@kvars-club.example, <span class="label">Website:</span> www.kvars-club.example</p>
    <p class="address-line"><span class="label">Address:</span> 42 Marwick Rd, Epsom, Auckland 1051</p>
  </div>
</section>

<section class="card card-back">
  <svg class="card-art" viewBox="0 0 838 384" aria-hidden="true">
    <defs>
      <linearGradient id="skyBack" x1="0" y1="0" x2="0" y2="1">
        <stop offset="0" stop-color="var(--sky-top)"/>
        <stop offset="1" stop-color="var(--sky-bottom)"/>
      </linearGradient>
    </defs>
    <rect width="838" height="384" fill="url(#skyBack)"/>
    <g fill="var(--snow)">
      <circle cx="26" cy="22" r="4"/><circle cx="96" cy="22" r="4"/>
      <circle cx="40" cy="90" r="4"/><circle cx="150" cy="70" r="4"/>
      <circle cx="215" cy="56" r="4"/><circle cx="270" cy="14" r="4"/>
      <circle cx="330" cy="44" r="4"/><circle cx="420" cy="20" r="4"/>
      <circle cx="488" cy="52" r="4"/><circle cx="560" cy="26" r="4"/>
      <circle cx="654" cy="24" r="4"/><circle cx="700" cy="94" r="4"/>
      <circle cx="760" cy="54" r="4"/><circle cx="805" cy="100" r="4"/>
      <circle cx="670" cy="160" r="4"/><circle cx="560" cy="236" r="4"/>
      <circle cx="610" cy="270" r="4"/><circle cx="300" cy="180" r="4"/>
    </g>
    <path d="M0,246 C150,214 300,200 420,228 C560,262 690,326 838,296 L838,384 L0,384 Z" fill="var(--snow)"/>
    <rect x="36" y="108" width="222" height="216" rx="10" fill="var(--gear-a)" opacity=".55" role="img" aria-label="Illustration of a pair of skis and two ski poles standing in the snow"/>
    <rect x="709" y="192" width="75" height="170" rx="30" fill="var(--gear-b)" opacity=".7" role="img" aria-label="Illustration of a snowboard standing upright in the snow"/>
  </svg>
  <div class="brand-name">KVARS</div>
  <div class="web-mark">WWW.KVARS-CLUB.EXAMPLE</div>
</section>

</body>
</html>
```